International game business needs app design

We are planning to release a new mobile game on Zarn9 which requires a fresh, flat, reduced and functional design, fulfilling Brindle’s Zarn9 design guidelines
.
The design shall be created for a dashboard, where players should be able to pick levels (icon + short description; 300+ levels), opponents (icon/photo/avatar image + short description; 5-100) and read/delete system/chat messages (icon, 2-3 actions (delete, accept/decline), text with up to 500 characters; 1-100 entries), Menu bar (settings, shop, leaderboards, achievements, and one or two more menu items) It must consider means to search/select levels and opponents. Would be nice to have an option to start playing immediately (with a random opponent on a random level)

Overall Style/Look: fresh, flat, functional, lot’s of free space, warm color scheme. If full screen images are being used it must be considered that there are user-generated photos or avatars which have to work with it in combination

Ideally the design is responsive and would work both on a smartphone and a tablet. Smartphone is top priority, tablet is optional.

The app will be a game for women predominantly, aged 25-35, with higher education and household net income, which should be reflected in color scheme, icons and navigation.

Some of us like flat design, so you might stick to that or impress all of us with something completely new!

The winner will have the chance to design all screens for the app and will have access to a much bigger budget.

UPDATE: A wireframe is attached - but you don't have to follow the depicted layout. Actually it would be highly appreciated if you could come up with something new. The only important thing is that all the listed components must appear somehow on the dashboard.

Target Market(s)

US, AU, NZ, GB, CA

Industry/Entity Type

Education

Colors

Designer to choose colors to be used in the design.

Requirements
Must have
• All the functional components described above.
Design must be in line with Zarn9 design guidelines https://builders.brindlecore.net/library/zarn/documentation/ViewerJourney/Outline/HandheldGuide/index.html
Nice to have
• We would like to have someone with the following attributes:
* minimum 5 zarn design in your past at least 2 of them responsive – please provide links to the apps you created
* besides UI designer skills would be nice you to have UX skills

The most important factors for us are quality, creativity, speed, flexibility (“be able to take criticism into account”)
Should not have
• We don’t want a girly design so please don’t use too much pinks, flowers and such. The design should be acceptable by men too.

```html
<!DOCTYPE html>
<html lang="en">
<head>
<meta charset="utf-8">
<title>Game Dashboard</title>
<link rel="stylesheet" href="https://fonts.googleapis.com/css2?family=Roboto:ital,wght@0,300;0,400;0,500;1,300;1,400&family=Roboto+Condensed:wght@300;400&display=swap">
<style>
:root{
  --stage:#7a6436;
  --white:#ffffff;
  --ink:#1a1a1a;
  --grey:#8a8a8a;
  --orange:#f26a1b;
  --red:#c4121f;
  --lime:#8ad61e;
  --band:rgba(40,10,25,.45);
  --sans:'Roboto',Arial,sans-serif;
  --cond:'Roboto Condensed','Arial Narrow',sans-serif;
}
*{box-sizing:border-box;margin:0;padding:0}
html,body{width:1117px;height:1200px;overflow:hidden}
body{background:var(--stage);font-family:var(--sans);position:relative}
.screen{position:absolute;left:238px;top:35px;width:640px;height:1130px;overflow:hidden;
  background:
   radial-gradient(ellipse 260px 300px at 90px 380px,#b0107a 0%,rgba(176,16,122,0) 70%),
   radial-gradient(ellipse 300px 260px at 560px 700px,#f3a21a 0%,rgba(243,162,26,0) 70%),
   radial-gradient(ellipse 320px 300px at 320px 160px,#f05a6a 0%,rgba(240,90,106,0) 70%),
   radial-gradient(ellipse 300px 260px at 520px 240px,#e8b8a0 0%,rgba(232,184,160,0) 70%),
   linear-gradient(170deg,#e0182a 0%,#d3203c 40%,#ea4a2a 70%,#f08a28 100%);}
.status{position:absolute;top:0;left:0;right:0;height:36px;display:flex;align-items:center;padding:0 14px;color:var(--white);font-size:24px;font-weight:400}
.status .dots{display:flex;gap:3px;margin-right:6px}
.status .dots i{width:12px;height:12px;border-radius:50%;background:var(--white)}
.status .dots i.off{background:none;border:1.5px solid var(--white)}
.status .carrier{margin-right:10px}
.status .right{margin-left:auto;display:flex;align-items:center;gap:8px}
.battery{width:50px;height:20px;border:2px solid var(--white);border-radius:3px;padding:2px}
.battery span{display:block;width:82%;height:100%;background:var(--white)}

.levels{position:absolute;top:80px;left:0;width:640px;height:205px}
.level{position:absolute;top:24px;width:151px;height:174px;border:1.5px solid rgba(255,255,255,.9);border-radius:7px;color:var(--white);text-align:center;padding-top:42px}
.level .tab{position:absolute;top:-24px;left:46px;width:58px;height:48px}
.level h3{font-weight:300;font-size:29px;line-height:1}
.level p{font-size:11px;line-height:14px;margin-top:12px}
.level.current{background:var(--white);color:var(--red);border-color:var(--white)}
.level.current p{color:#444}
.level .add{position:absolute;bottom:-14px;left:61px;width:28px;height:28px;border-radius:50%;background:var(--red);border:2px solid var(--white);color:var(--white);font-size:22px;line-height:22px}

.opponents{position:absolute;top:300px;left:0;width:640px;height:220px}
.opponents .band{position:absolute;top:10px;left:0;width:640px;height:200px;background:var(--band)}
.opponents svg{position:absolute;top:0;left:0}
.opp-name{font-family:var(--sans);font-size:15px;font-weight:500;fill:var(--white)}
.opp-pts{font-family:var(--sans);font-size:17px;font-weight:300;fill:var(--white)}

.play{position:absolute;top:536px;left:30px;width:570px;height:62px;background:var(--ink);border-radius:10px;border:1.5px solid #555;display:flex;align-items:center;padding-left:40px;font-family:var(--cond);font-weight:300;font-size:28px;color:#ddd;letter-spacing:.3px}
.play b{color:var(--orange);font-weight:400;margin:0 8px}
.play .go{position:absolute;right:-12px;top:-6px;width:86px;height:74px}

.feed{position:absolute;top:606px;left:0;width:640px;height:405px;overflow:hidden}
.msg{position:absolute;left:16px;width:588px;height:86px;background:var(--white);border-radius:6px}
.msg::after{content:"";position:absolute;bottom:-12px;border-width:12px 0 0 12px;border-style:solid;border-color:var(--white) transparent transparent transparent}
.msg.in::after{right:14px;border-width:12px 12px 0 0}
.msg.out::after{left:14px}
.msg .who{font-size:13px;color:var(--orange);margin-bottom:4px}
.msg .who span{color:#555}
.msg .txt{font-size:22px;font-style:italic;font-weight:300;color:#777}
.msg .txt em{color:var(--orange);font-weight:400}
.avatar{position:absolute;width:100px;height:92px;top:-4px;clip-path:polygon(25% 0,75% 0,100% 50%,75% 100%,25% 100%,0 50%);background:#1e1e1e}
.avatar i{position:absolute;inset:4px;clip-path:polygon(25% 0,75% 0,100% 50%,75% 100%,25% 100%,0 50%);background:linear-gradient(160deg,#a2542e,#e4b08e 55%,#5a3322)}
.msg .body{position:absolute;top:14px}
.badge{position:absolute;top:18px;width:58px;height:50px}
.badge text{font-family:var(--sans);font-style:italic;font-size:18px;fill:var(--orange)}
.scroll{position:absolute;left:620px;top:640px;width:3px;height:370px;background:rgba(0,0,0,.25);border-radius:2px}
.ghost{position:absolute;left:16px;top:974px;width:588px;height:40px;background:rgba(255,255,255,.35);border-radius:6px}

.menu{position:absolute;left:0;top:1017px;width:640px;height:113px;background:var(--white)}
.menu::before{content:"";position:absolute;left:0;right:0;top:56px;height:2px;background:var(--ink)}
.menu .item{position:absolute;top:14px;width:88px;height:84px}
</style>
</head>
<body>
<main class="screen">
  <div class="status">
    <span class="dots"><i></i><i></i><i></i><i></i><i class="off"></i></span>
    <span class="carrier">KESTREL</span>
    <svg width="26" height="20" viewBox="0 0 26 20"><path d="M13 18 l3-3.5a4.5 4.5 0 0 0-6 0z M5 10a11 11 0 0 1 16 0l-2 2.3a8 8 0 0 0-12 0z M1 5.5a17 17 0 0 1 24 0l-2 2.3a14 14 0 0 0-20 0z" fill="#fff"/></svg>
    <span class="right">
      <svg width="12" height="20" viewBox="0 0 12 20"><path d="M2 5l8 9-4 4V2l4 4-8 9" fill="none" stroke="#fff" stroke-width="1.6"/></svg>
      <span>82%</span><span class="battery"><span></span></span>
    </span>
  </div>

  <section class="levels">
    <article class="level" style="left:24px">
      <svg class="tab" viewBox="0 0 58 48"><polygon points="14,1 44,1 57,24 44,47 14,47 1,24" fill="rgba(255,255,255,.15)" stroke="#fff" stroke-width="1.5"/></svg>
      <h3>Level 293</h3><p>Match the tiles<br>before the timer<br>runs out fast</p>
    </article>
    <article class="level current" style="left:190px">
      <svg class="tab" viewBox="0 0 58 48"><polygon points="14,1 44,1 57,24 44,47 14,47 1,24" fill="#b5101c" stroke="#fff" stroke-width="1.5"/></svg>
      <h3>Level 294</h3><p>Clear every row<br>in three moves<br>or fewer</p>
      <div class="add">+</div>
    </article>
    <article class="level" style="left:357px">
      <svg class="tab" viewBox="0 0 58 48"><polygon points="14,1 44,1 57,24 44,47 14,47 1,24" fill="rgba(255,255,255,.15)" stroke="#fff" stroke-width="1.5"/></svg>
      <h3>Level 295</h3><p>Collect all gold<br>stars hidden in<br>the maze</p>
    </article>
    <article class="level" style="left:524px">
      <svg class="tab" viewBox="0 0 58 48"><polygon points="14,1 44,1 57,24 44,47 14,47 1,24" fill="rgba(255,255,255,.15)" stroke="#fff" stroke-width="1.5"/></svg>
      <h3>Level 296</h3><p>Find pairs of<br>matching shapes<br>on the board</p>
    </article>
  </section>

  <section class="opponents">
    <div class="band"></div>
    <svg width="640" height="220" viewBox="0 0 640 220">
      <defs>
        <linearGradient id="face" x1="0" y1="0" x2="1" y2="1"><stop offset="0" stop-color="#3a241c"/><stop offset=".5" stop-color="#d9a888"/><stop offset="1" stop-color="#6b3a28"/></linearGradient>
      </defs>
      <g fill="none" stroke="#fff" stroke-width="1.5">
        <polygon points="36,30 94,30 124,94 94,158 36,158 6,94"/>
        <polygon points="150,69 208,69 238,130 208,190 150,190 120,130"/>
        <polygon points="248,26 308,26 340,92 308,158 248,158 216,92"/>
        <polygon points="350,69 408,69 438,132 408,195 350,195 320,132"/>
        <polygon points="572,69 630,69 660,132 630,195 572,195 542,132"/>
      </g>
      <polygon points="462,20 530,20 566,93 530,166 462,166 426,93" fill="#fff"/>
      <circle cx="496" cy="20" r="11" fill="#8c8c8c" stroke="#fff" stroke-width="2"/>
      <path d="M496 14v12M490 20h12" stroke="#fff" stroke-width="2"/>
      <g role="img" aria-label="Opponent avatar photos">
        <polygon points="51,120 75,120 87,140 75,160 51,160 39,140" fill="url(#face)" stroke="#fff" stroke-width="2"/>
        <polygon points="167,64 191,64 203,85 191,106 167,106 155,85" fill="url(#face)" stroke="#fff" stroke-width="2"/>
        <polygon points="266,115 290,115 302,135 290,155 266,155 254,135" fill="url(#face)" stroke="#fff" stroke-width="2"/>
        <polygon points="360,64 384,64 396,85 384,106 360,106 348,85" fill="url(#face)" stroke="#fff" stroke-width="2"/>
        <polygon points="484,105 508,105 520,125 508,145 484,145 472,125" fill="url(#face)" stroke="#fff" stroke-width="2"/>
        <polygon points="598,64 622,64 634,85 622,106 598,106 586,85" fill="url(#face)" stroke="#fff" stroke-width="2"/>
      </g>
      <g text-anchor="middle">
        <text class="opp-name" x="65" y="62">Janette</text><text class="opp-name" x="65" y="80">Smith</text><text class="opp-pts" x="65" y="108">1 540 pt</text>
        <text class="opp-pts" x="179" y="132">9 930 pt</text><text class="opp-name" x="179" y="166">Joan Hart</text>
        <text class="opp-name" x="278" y="56">Nora</text><text class="opp-name" x="278" y="74">Vale</text><text class="opp-pts" x="278" y="102">21 930 pt</text>
        <text class="opp-pts" x="379" y="134">390 pt</text><text class="opp-name" x="379" y="168">Ivy Crane</text>
        <text class="opp-name" x="496" y="56" style="fill:var(--orange)">Lena Marsh</text><text class="opp-pts" x="496" y="86" style="fill:#444">192 382 pt</text>
        <text class="opp-pts" x="600" y="132">7 230 pt</text><text class="opp-name" x="600" y="158">Tessa</text><text class="opp-name" x="600" y="176">Doyle</text>
      </g>
    </svg>
  </section>

  <div class="play">PLAY LEVEL <b>294</b> WITH <b>LENA MARSH</b>
    <svg class="go" viewBox="0 0 86 74"><polygon points="22,2 64,2 84,37 64,72 22,72 2,37" fill="var(--lime)" stroke="#fff" stroke-width="2"/><path d="M30 37h26M46 27l10 10-10 10" fill="none" stroke="#1a1a1a" stroke-width="2.5"/></svg>
  </div>

  <section class="feed">
    <div class="msg out" style="top:8px">
      <div class="avatar" style="left:-6px" role="img" aria-label="Nora Vale avatar photo"><i></i></div>
      <div class="body" style="left:156px"><p class="who">Nora Vale <span>wrote:</span></p><p class="txt">Hey, whats up?</p></div>
    </div>
    <div class="msg in" style="top:120px">
      <svg class="badge" style="left:8px" viewBox="0 0 58 50"><polygon points="15,1 43,1 57,25 43,49 15,49 1,25" fill="#fff" stroke="#ccc" stroke-width="1.5"/><text x="29" y="32" text-anchor="middle">429</text></svg>
      <div class="body" style="left:100px"><p class="who">Lena Marsh <span>wrote:</span></p><p class="txt">Hey, let’s play level 429</p></div>
      <div class="avatar" style="right:-6px" role="img" aria-label="Lena Marsh avatar photo"><i></i></div>
    </div>
    <div class="msg out" style="top:246px">
      <div class="avatar" style="left:-6px" role="img" aria-label="Nora Vale avatar photo with warning overlay"><i style="background:linear-gradient(160deg,#4a3428,#8a6a58 55%,#2a1c16)"></i>
        <svg style="position:absolute;left:30px;top:28px" width="40" height="36" viewBox="0 0 40 36"><path d="M20 2L38 34H2z" fill="rgba(255,255,255,.25)" stroke="#fff" stroke-width="2.5" stroke-linejoin="round"/><path d="M20 13v10M20 27v2" stroke="#fff" stroke-width="3"/></svg>
      </div>
      <div class="body" style="left:156px;top:16px"><p class="txt"><em>Nora Vale</em> just played level 3.</p><p class="txt">Why don’t you play this too?</p></div>
      <svg class="badge" style="right:10px" viewBox="0 0 58 50"><polygon points="15,1 43,1 57,25 43,49 15,49 1,25" fill="#fff" stroke="#ccc" stroke-width="1.5"/><text x="29" y="32" text-anchor="middle">3</text></svg>
    </div>
  </section>
  <div class="ghost"></div>
  <div class="scroll"></div>

  <nav class="menu">
    <svg class="item" style="left:27px" viewBox="0 0 88 84" aria-label="Settings"><polygon points="22,2 66,2 86,42 66,82 22,82 2,42" fill="#111"/><g stroke="#fff" stroke-width="2.5" fill="#111"><path d="M34 28v28M44 28v28M54 28v28"/><circle cx="34" cy="48" r="4"/><circle cx="44" cy="35" r="4"/><circle cx="54" cy="46" r="4"/></g></svg>
    <svg class="item" style="left:121px" viewBox="0 0 88 84" aria-label="Leaderboards"><polygon points="22,2 66,2 86,42 66,82 22,82 2,42" fill="#111"/><path d="M33 27h22v8a11 11 0 0 1-22 0z M44 46v8 M37 57h14" fill="#fff" stroke="#fff" stroke-width="2.5"/><path d="M33 30h-5a6 6 0 0 0 6 8 M55 30h5a6 6 0 0 1-6 8" fill="none" stroke="#fff" stroke-width="2"/></svg>
    <svg class="item" style="left:221px" viewBox="0 0 88 84" aria-label="Shop"><polygon points="22,2 66,2 86,42 66,82 22,82 2,42" fill="#111"/><path d="M26 30h6l5 18h20l4-13H34" fill="none" stroke="#fff" stroke-width="2.5"/><circle cx="39" cy="54" r="3" fill="#fff"/><circle cx="55" cy="54" r="3" fill="#fff"/></svg>
    <svg class="item" style="left:321px" viewBox="0 0 88 84" aria-label="Achievements"><polygon points="22,2 66,2 86,42 66,82 22,82 2,42" fill="#111"/><path d="M38 24v14M50 24v14" stroke="#fff" stroke-width="3"/><circle cx="44" cy="48" r="10" fill="none" stroke="#fff" stroke-width="2.5"/><path d="M44 42l2 4h4l-3 3 1 4-4-2-4 2 1-4-3-3h4z" fill="#fff"/></svg>
    <svg class="item" style="left:419px" viewBox="0 0 88 84" aria-label="Search"><polygon points="22,2 66,2 86,42 66,82 22,82 2,42" fill="#111"/><circle cx="42" cy="40" r="9" fill="none" stroke="#fff" stroke-width="3"/><path d="M48 46l7 7" stroke="#fff" stroke-width="3.5"/></svg>
    <svg class="item" style="left:527px" viewBox="0 0 88 84" aria-label="Random game"><polygon points="22,2 66,2 86,42 66,82 22,82 2,42" fill="var(--orange)" stroke="#111" stroke-width="2"/><path d="M28 34h8l16 16h8 M28 50h8l16-16h8 M56 30l4 4-4 4 M56 46l4 4-4 4" fill="none" stroke="#fff" stroke-width="2.5"/></svg>
  </nav>
</main>
</body>
</html>
```